DL size flyer for Autism Consultancy website

We need a printed flyer DL size ( 210mmx99mm) for our Autism Consultancy website www.brightpathkids.nz which provides therapy for autistic children.
I want the flyer to look consistent with the website’s design. Please feel free to use the colour scheme, fonts, icons or any images from www.brightpathkids.nz.It should be easy to see “Autism” or “Autistic” word from a distance.
Please use either an oversized logo or make “Do you have a verbal and able autistic child?” more prominent.
Please do not convert the text fields to outlines, i.e. I need to be able to edit any text after.The final design should be either in Adobe Illustrator or Adobe Photoshop format.
The Specs for the flyer are
Document Trim Size99 x 210 mm 1169 x 2480 pixels
Full Bleed Size102 x 213 mm 1205 x 2516 pixels
Our Logo https://1drv.ms/u/s!AoH0rRjDY2GYg6QtU-xjoVlmslKp6gPlease
use this photo for the front side https://qzdropbin.io/f/Pw4KcN8rTyH2mXs6BvLd9QeFz1Gj
another one for reverse
https://qzdropbin.io/f/Rk2HsV5nWqJ7tZc3MfXb8LpYd4Ne
Please use the following content:
Do you have a verbal and able autistic child?
We use child-centred, modern and innovative approaches
Teaching autistic children to bond, laugh and play.
We work with schools
We help autistic children to develop social minds
We offer:
• Specialist assessments
• Consultations for parents & schools
• Social learning programmes
• Social-cognitive therapy
We can create an individual learning path, best suited for your child.
Our programmes and interventions include:
• Chatter Quest
• Peer Bright
• Team Puzzles
• Tingle Words
• Pebble Tales
• Pembrook Speech Ladder
• Vorlin Method
• BRIMLE Method
• Tandem Pattern Coaching
contact details on both sides:
www.brightpathkids.nz
info@brightpathkids.nz
(09) 57-318-46

```html
<!DOCTYPE html>
<html lang="en">
<head>
<meta charset="utf-8">
<title>Bright Path Kids – DL Flyer</title>
<link href="https://fonts.googleapis.com/css2?family=Righteous&family=Lato:wght@400;700&display=swap" rel="stylesheet">
<style>
  :root{
    --stage:#333333;
    --navy:#172a5a;
    --yellow:#fcd32a;
    --white:#ffffff;
    --ink:#111111;
    --photo-light:#ecebea;
    --photo-warm:#d9a988;
  }
  *{margin:0;padding:0;box-sizing:border-box}
  html,body{width:1200px;height:1200px;overflow:hidden;background:var(--stage)}
  .canvas{position:relative;width:1200px;height:1200px}
  .flyer{position:absolute;top:242px;width:361px;height:741px;background:var(--white);overflow:hidden;font-family:"Lato",sans-serif}
  .flyer--front{left:175px}
  .flyer--back{left:639px}
  .display{font-family:"Righteous",sans-serif;font-weight:400}

  /* front */
  .front-photo{position:absolute;inset:0 0 auto 0;height:530px;
    background:linear-gradient(160deg,var(--photo-light) 0%,#e7e2dc 40%,var(--photo-warm) 100%)}
  .front-shapes{position:absolute;left:0;top:0}
  .brand{position:absolute;left:30px;top:30px;display:flex;align-items:center;gap:12px}
  .brand__dot{width:40px;height:40px;border-radius:50%;background:var(--yellow)}
  .brand__name{font-family:"Righteous",sans-serif;color:var(--navy);font-size:25px}
  .question{position:absolute;left:59px;top:402px;width:240px;height:240px;border-radius:50%;
    background:var(--navy);color:var(--yellow);display:flex;align-items:center;justify-content:center;
    text-align:center;font-size:31px;line-height:38px;letter-spacing:.5px}
  .intro{position:absolute;left:28px;top:650px;width:310px;font-size:10.4px;line-height:13px;color:var(--ink)}
  .footer{position:absolute;left:0;bottom:0;width:100%;height:42px;background:var(--yellow);
    display:flex;align-items:center;justify-content:center;font-size:14px;letter-spacing:.6px;color:var(--ink)}

  /* back */
  .back-photo{position:absolute;inset:0 0 auto 0;height:260px;
    background:linear-gradient(135deg,#c69a70 0%,#e6c9a8 45%,#d9554a 85%,#f1f1f1 100%)}
  .back-shapes{position:absolute;left:0;top:0}
  .help-title{position:absolute;top:286px;left:0;width:100%;text-align:center;color:var(--yellow);font-size:34px;padding-left:38px}
  .step__badge{position:absolute;left:31px;width:48px;height:48px;border-radius:50%;background:var(--yellow);
    color:var(--navy);font-family:"Righteous",sans-serif;font-size:26px;display:flex;align-items:center;justify-content:center;
    box-shadow:1px 2px 3px rgba(0,0,0,.25)}
  .step__label{position:absolute;left:18px;width:82px;text-align:center;color:var(--navy);font-family:"Righteous",sans-serif;font-size:20px;line-height:24px}
  .step__text{position:absolute;left:108px;width:244px;font-size:12.8px;line-height:16px;color:var(--ink);
    hyphens:auto;-webkit-hyphens:auto}
</style>
</head>
<body>
<div class="canvas">

  <section class="flyer flyer--front">
    <div class="front-photo" role="img" aria-label="Photo: a therapist facing a smiling boy holding a teddy bear in a bright playroom"></div>
    <svg class="front-shapes" width="361" height="741" viewBox="0 0 361 741" aria-hidden="true">
      <path d="M0 512 C120 520 270 470 361 400 L361 741 L0 741 Z" fill="var(--yellow)"/>
      <path d="M0 527 C140 535 280 500 361 455 L361 741 L0 741 Z" fill="var(--white)"/>
    </svg>
    <div class="brand">
      <span class="brand__dot"></span>
      <span class="brand__name">Bright Path Kids</span>
    </div>
    <h1 class="question display">Do you<br>have a verbal<br>&amp;<br>able autistic<br>child?</h1>
    <p class="intro">The consultancy specializes in the primary school age, verbal and able autistic children, also referred to as high-functioning autistic children, as well as children with Asperger's syndrome.</p>
    <div class="footer">www.brightpathkids.nz</div>
  </section>

  <section class="flyer flyer--back">
    <div class="back-photo" role="img" aria-label="Photo: a young boy in a striped shirt lying on the floor playing with toy cars"></div>
    <svg class="back-shapes" width="361" height="741" viewBox="0 0 361 741" aria-hidden="true">
      <path d="M0 245 C120 180 260 190 361 245 L361 741 L0 741 Z" fill="var(--white)"/>
      <path d="M0 245 C120 180 260 190 361 245 L361 258 C250 215 110 220 0 322 Z" fill="var(--navy)"/>
    </svg>
    <h2 class="help-title display">How We Help ?</h2>

    <div class="step__badge" style="top:348px">1.</div>
    <div class="step__label" style="top:404px">Analyse</div>
    <p class="step__text" style="top:349px">We work closely with parents and educators to offer a comprehensive analysis of the sensory and social-emotional difficulties that hinder the child's social wellbeing and academic development</p>

    <div class="step__badge" style="top:468px">2.</div>
    <div class="step__label" style="top:527px">Consult</div>
    <p class="step__text" style="top:458px">We offer consultations to improve social and emotional wellbeing of autistic children through the relevant accommodations, proven modern autism approaches and essential therapies offered by the specialists in other areas</p>

    <div class="step__badge" style="top:598px">3.</div>
    <div class="step__label" style="top:656px">Develop</div>
    <p class="step__text" style="top:578px">We provide modern autism programmes that employ social interest, social motivation and social memory to improve social engagement, emotional understanding, social problem solving and other key parts of social and emotional intelligence</p>

    <div class="footer">www.brightpathkids.nz</div>
  </section>

</div>
</body>
</html>
```